Bref créative
Brookmere
Brookmere Vale Baptist Church
Simple
Dolores Lomax
Communications
4163 Ambervale Road
Regina SK S7N 3K8
dolores@brookmerechapel.ca
brookmerechapel.ca
We will need business cards, letterhead and envelopes.
Our Logo
ai file

```html
<!DOCTYPE html>
<html lang="en">
<head>
<meta charset="utf-8">
<title>Brookmere Vale Baptist Church — Stationery</title>
<link href="https://fonts.googleapis.com/css2?family=Cinzel:wght@500&family=Open+Sans:wght@400;600&display=swap" rel="stylesheet">
<style>
  :root{
    --stage:#9c9c9c;
    --paper:#ffffff;
    --brand-blue:#1f7fc0;
    --blue-light:#6cc3ef;
    --blue-dark:#1565a8;
    --gold:#c9a63e;
    --gold-light:#e6cf86;
    --ink:#4a4a4a;
    --muted:#8a8a8a;
    --watermark:#eef1f4;
  }
  *{margin:0;padding:0;box-sizing:border-box}
  html,body{width:1200px;height:743px;overflow:hidden}
  body{background:var(--stage);font-family:"Open Sans",Arial,sans-serif;color:var(--ink);position:relative}
  .sheet{position:absolute;background:var(--paper);box-shadow:0 2px 6px rgba(0,0,0,.25)}
  .wordmark{font-family:"Cinzel",Georgia,serif;font-weight:500;color:var(--brand-blue);letter-spacing:.5px;line-height:1;white-space:nowrap}
  .tagline{font-size:5px;letter-spacing:1.4px;color:var(--muted);text-transform:uppercase;margin-top:3px;white-space:nowrap}
  .contact{font-size:6px;line-height:1.55;color:var(--ink);white-space:nowrap}

  /* Envelope */
  .envelope{left:96px;top:84px;width:437px;height:564px}
  .envelope .brand{position:absolute;left:18px;top:24px}
  .envelope .brand .wordmark{font-size:22px}
  .envelope .contact{position:absolute;left:20px;top:58px}
  .envelope .gold-rule{position:absolute;left:0;top:160px;width:100%;height:3px;background:var(--gold)}
  .envelope .blue-band{position:absolute;left:0;top:165px;width:100%;height:17px;background:linear-gradient(90deg,var(--blue-light),var(--brand-blue) 60%,var(--blue-dark))}
  .flap{position:absolute;left:0;width:437px;height:90px}
  .flap-blue{top:199px}.flap-gold{top:300px}.flap-white{top:403px}
  .flap .wordmark{position:absolute;left:0;right:0;top:32px;text-align:center;font-size:19px}
  .flap-white .wordmark{top:33px;font-size:18px}

  /* Letterhead */
  .letterhead{left:552px;top:108px;width:391px;height:509px}
  .letterhead .brand{position:absolute;left:14px;top:30px}
  .letterhead .brand .wordmark{font-size:21px}
  .letterhead .contact{position:absolute;left:226px;top:30px;font-size:5.5px}
  .letterhead .watermark{position:absolute;left:0;right:0;top:240px;text-align:center;font-family:"Cinzel",Georgia,serif;font-size:40px;color:var(--watermark);white-space:nowrap}
  .letterhead .gold-rule{position:absolute;left:0;top:478px;width:100%;height:2px;background:var(--gold)}
  .letterhead .blue-band{position:absolute;left:0;top:483px;width:100%;height:18px;background:linear-gradient(90deg,var(--blue-light),var(--brand-blue) 60%,var(--blue-dark));color:#fff;font-size:5.5px;text-align:center;line-height:18px}

  /* Business card */
  .card{left:967px;top:197px;width:163px;height:96px}
  .card .brand{position:absolute;right:14px;top:12px;text-align:center}
  .card .brand .wordmark{font-size:13px}
  .card .brand .tagline{font-size:3.5px;letter-spacing:1px;margin-top:2px}
  .card .person{position:absolute;left:14px;top:46px;font-size:5px;line-height:1.5;white-space:nowrap}
  .card .person strong{font-weight:600;color:var(--ink)}
  .card .contact{position:absolute;left:91px;top:46px;font-size:3.8px}
</style>
</head>
<body>

<section class="sheet envelope" aria-label="Envelope">
  <div class="brand">
    <div class="wordmark">Brookmere</div>
    <div class="tagline">Vale Baptist Church</div>
  </div>
  <div class="contact">
    4163 Ambervale Road · Regina SK S7N 3K8<br>
    Phone 306 555 0148 · Fax 306 555 0149<br>
    dolores@brookmerechapel.ca
  </div>
  <div class="gold-rule"></div>
  <div class="blue-band"></div>

  <svg class="flap flap-blue" viewBox="0 0 437 90" aria-hidden="true">
    <defs>
      <linearGradient id="flapBlue" x1="0" x2="1">
        <stop offset="0" stop-color="#8ad3f5"/><stop offset=".55" stop-color="#2e8fd0"/><stop offset="1" stop-color="#1565a8"/>
      </linearGradient>
      <linearGradient id="flapGold" x1="0" x2="1">
        <stop offset="0" stop-color="#b8912b"/><stop offset=".5" stop-color="#e6cf86"/><stop offset="1" stop-color="#b08a28"/>
      </linearGradient>
    </defs>
    <path d="M0,0H437V20Q437,30 425,40L400,75Q392,89 375,89H62Q45,89 37,75L12,40Q0,30 0,20Z" fill="url(#flapBlue)"/>
  </svg>
  <div class="flap flap-blue"><div class="wordmark" style="color:var(--blue-dark)">Brookmere</div></div>

  <svg class="flap flap-gold" viewBox="0 0 437 90" aria-hidden="true">
    <path d="M0,0H437V20Q437,30 425,40L400,75Q392,89 375,89H62Q45,89 37,75L12,40Q0,30 0,20Z" fill="url(#flapGold)"/>
  </svg>
  <div class="flap flap-gold"><div class="wordmark">Brookmere</div></div>

  <svg class="flap flap-white" viewBox="0 0 437 90" aria-hidden="true">
    <path d="M0,0H437V20Q437,30 425,40L400,75Q392,89 375,89H62Q45,89 37,75L12,40Q0,30 0,20Z" fill="#fff" stroke="#d6d6d6" stroke-width="1"/>
  </svg>
  <div class="flap flap-white"><div class="wordmark">Brookmere</div></div>
</section>

<section class="sheet letterhead" aria-label="Letterhead">
  <div class="brand">
    <div class="wordmark">Brookmere</div>
    <div class="tagline">Vale Baptist Church</div>
  </div>
  <div class="contact">
    4163 Ambervale Road<br>
    Regina SK S7N 3K8<br>
    Phone 306 555 0148<br>
    Fax 306 555 0149<br>
    dolores@brookmerechapel.ca
  </div>
  <div class="watermark">Brookmere</div>
  <div class="gold-rule"></div>
  <div class="blue-band">brookmerechapel.ca</div>
</section>

<section class="sheet card" aria-label="Business card">
  <div class="brand">
    <div class="wordmark">Brookmere</div>
    <div class="tagline">Vale Baptist Church</div>
  </div>
  <div class="person"><strong>Dolores Lomax</strong><br>Communications</div>
  <div class="contact">
    4163 Ambervale Road<br>
    Regina SK S7N 3K8<br>
    Phone 306 555 0148<br>
    Fax 306 555 0149<br>
    dolores@brookmerechapel.ca
  </div>
</section>

</body>
</html>
```